Email Template for AI Website Builder Marketing Campaign

Update: All the designs submitted have too much content for an email template. I have attached a mockup example of a simplified design. Please follow this guideline to revise your design to be less "wordy" and have less content to optimize the delivery rate of the emails. I have also attached the images I used to create the mockup. Feel free to use these images for your revised designs.
Original Brief:
I need a catchy email template for my new AI Website Builder, FolioNova.ai. The template must be professional, colorful, yet not too complex. The concept of the product is this:
FolioNova uses Artificial Intelligence (AI) to instantly build stunning websites, absolutely FREE. The user simply specifies their business name and business category (industry), and their stunning new website appears before their eyes!
The template will be used in MailChimp, so please provide the code that I can simply paste into the email body.
Here is a screenshot of our new website (which is not online yet) so you can match the color scheme and style of the email template to the new website design:
https://brindlemesh.com/mock_img/7720518/2638140/58190374/q8rt2lbw4k7ehnpyd3umc0xsvo_image.jpg
Let me know if you have any questions.
Thanks!
All submitted designs are too lengthy (too much content) for an email template. I will provide a mockup showing a sample of how you can simplify your design to function better as an email template and better suit my needs. I appreciate your patience!

```html
<!DOCTYPE html>
<html lang="en">
<head>
<meta charset="utf-8">
<title>FolioNova – AI Website Builder Email</title>
<link rel="stylesheet" href="https://fonts.googleapis.com/css2?family=Inter:wght@400;500;600;700;800&display=swap">
<style>
  :root {
    --page-bg: #cccccc;
    --navy-deep: #06153f;
    --navy: #0a2366;
    --royal: #0f5cf0;
    --royal-dark: #0b2a78;
    --cyan: #2bc3f5;
    --cyan-bright: #35d0ff;
    --white: #ffffff;
    --ink: #101010;
    --ink-soft: #3a3a3a;
    --grey: #9a9a9a;
    --grey-link: #7c7c7c;
    --icon-grey: #b9b9b9;
  }
  * { box-sizing: border-box; margin: 0; padding: 0; }
  html, body {
    width: 814px; height: 1200px; overflow: hidden;
    background: var(--page-bg);
    font-family: "Inter", Arial, sans-serif;
  }
  .email {
    position: absolute; left: 204px; top: 43px;
    width: 407px; height: 1114px;
    background: var(--white);
    overflow: hidden;
  }

  /* Hero */
  .hero {
    position: absolute; left: 0; top: 0; width: 407px; height: 582px;
    background: linear-gradient(160deg, var(--navy-deep) 0%, #0a1f5e 45%, var(--navy) 100%);
  }
  .hero-art {
    position: absolute; right: 0; top: 0; width: 180px; height: 298px;
    background: radial-gradient(ellipse at 70% 40%, rgba(60,110,200,0.45) 0%, rgba(30,60,140,0.2) 50%, rgba(10,30,90,0) 80%);
  }
  .brand {
    position: absolute; left: 0; width: 100%;
    display: flex; align-items: center; justify-content: center; gap: 7px;
    font-weight: 600; font-size: 21px; letter-spacing: -0.2px;
  }
  .brand-dot {
    width: 20px; height: 20px; border-radius: 50%;
    background: var(--cyan);
  }
  .hero .brand { top: 24px; color: var(--white); }
  .hero-title {
    position: absolute; left: 43px; top: 86px;
    color: var(--white); font-weight: 400; font-size: 28.5px; line-height: 30.5px;
    letter-spacing: -0.2px;
  }
  .hero-title strong { color: var(--cyan-bright); font-weight: 700; }
  .btn {
    position: absolute; display: flex; align-items: center; justify-content: center;
    font-size: 12.5px; font-weight: 500; color: var(--white); border-radius: 2px;
    text-decoration: none;
  }
  .btn-solid { background: linear-gradient(90deg, var(--cyan-bright), #1c9ff0); }
  .hero .btn { left: 43px; top: 204px; width: 175px; height: 33px; }

  /* Feature card */
  .feature-card {
    position: absolute; left: 43px; top: 299px; width: 364px; height: 223px;
    background: var(--white); border-radius: 5px 0 0 5px;
  }
  .eyebrow { position: absolute; font-size: 9px; font-weight: 500; }
  .feature-card .eyebrow { left: 31px; top: 28px; color: var(--cyan); }
  .feature-title {
    position: absolute; left: 31px; top: 44px;
    font-size: 20.5px; line-height: 24px; font-weight: 400; color: var(--ink);
  }
  .feature-title b { font-weight: 800; }
  .feature-text {
    position: absolute; left: 31px; top: 102px; width: 200px;
    font-size: 10.3px; line-height: 15px; color: var(--ink-soft);
  }
  .feature-card .btn { left: 31px; top: 161px; width: 111px; height: 34px; font-size: 12px; }
  .feature-visual {
    position: absolute; left: 232px; top: 21px; width: 132px; height: 183px;
    background: linear-gradient(160deg, #e7f3fb 0%, #1d3350 45%, #3b5c86 75%, #eef2f6 100%);
    border-radius: 60px 0 0 20px;
  }

  /* Article band */
  .article {
    position: absolute; left: 0; top: 582px; width: 407px; height: 293px;
    background: linear-gradient(180deg, var(--royal) 0%, #0b45c9 40%, var(--royal-dark) 75%, #071f63 100%);
  }
  .article-art {
    position: absolute; left: 0; top: 41px; width: 81px; height: 210px;
    background: radial-gradient(ellipse at 20% 50%, rgba(170,210,255,0.55) 0%, rgba(90,150,240,0.2) 55%, rgba(20,60,160,0) 80%);
  }
  .article .eyebrow { left: 108px; top: 44px; color: var(--white); font-size: 10.8px; }
  .article-title {
    position: absolute; left: 108px; top: 63px; width: 280px;
    color: var(--white); font-size: 21.7px; line-height: 26px; font-weight: 700;
  }
  .article-text {
    position: absolute; left: 108px; top: 150px; width: 240px;
    color: var(--white); font-size: 10.9px; line-height: 15px;
  }
  .btn-outline {
    border: 1px solid var(--cyan-bright); background: transparent; border-radius: 3px;
  }
  .article .btn { left: 108px; top: 200px; width: 111px; height: 34px; font-size: 12px; }

  /* Footer */
  .footer {
    position: absolute; left: 0; top: 875px; width: 407px; height: 239px;
    background: var(--white); border-top: 1px solid var(--cyan);
  }
  .footer .brand { top: 45px; color: var(--ink); }
  .footer-text {
    position: absolute; left: 60px; top: 91px; width: 287px;
    text-align: center; color: var(--grey); font-size: 9.5px; line-height: 13.6px;
  }
  .footer-links {
    position: absolute; left: 0; top: 140px; width: 100%;
    display: flex; justify-content: center; font-size: 8.8px; color: var(--grey-link);
  }
  .footer-links span { padding: 0 4px; border-right: 1px solid var(--grey-link); line-height: 10px; }
  .footer-links span:last-child { border-right: none; }
  .social {
    position: absolute; left: 57px; top: 174px; display: flex; gap: 11.2px;
  }
  .social-dot { width: 20px; height: 20px; border-radius: 50%; background: var(--icon-grey); }
</style>
</head>
<body>
<main class="email">
  <section class="hero">
    <div class="hero-art" role="img" aria-label="Digital circuit-style head illustration fading into the background"></div>
    <div class="brand"><span class="brand-dot"></span>FolioNova</div>
    <h1 class="hero-title">Let Artificial Intelligence<br>Build Your <strong>Stunning</strong><br>Website <strong>Instantly</strong></h1>
    <a class="btn btn-solid" href="#">Build My Free Website</a>

    <article class="feature-card">
      <p class="eyebrow">AI Website Generator</p>
      <h2 class="feature-title">Build a Website<br><b>With AI.</b></h2>
      <p class="feature-text">Harness The Power Of Artificial Intelligence With FolioNova!<br>It's The Future Of Website Building!</p>
      <a class="btn btn-solid" href="#">Learn More</a>
      <div class="feature-visual" role="img" aria-label="Stacked website page layers beneath a glowing product badge"></div>
    </article>
  </section>

  <section class="article">
    <div class="article-art" role="img" aria-label="Wireframe line illustration of a human head in profile"></div>
    <p class="eyebrow">Advancements In AI</p>
    <h2 class="article-title">Technology and<br>Their Influence on<br>Website Building</h2>
    <p class="article-text">Over The Past Decade. AI's Capabilities Have Grown Exponentially, Transcending From...</p>
    <a class="btn btn-outline" href="#">Learn More</a>
  </section>

  <footer class="footer">
    <div class="brand"><span class="brand-dot"></span>FolioNova</div>
    <p class="footer-text">It'll Take Minutes Or Less! A Few Simple Steps Will Take You Through Image Selection, Content Generation, Color Scheme, And Layout!</p>
    <nav class="footer-links"><span>Unsubscribe</span><span>Terms &amp; Conditions</span><span>Privacy Policy</span></nav>
    <div class="social" aria-label="Social links">
      <span class="social-dot"></span><span class="social-dot"></span><span class="social-dot"></span><span class="social-dot"></span><span class="social-dot"></span>
      <span class="social-dot"></span><span class="social-dot"></span><span class="social-dot"></span><span class="social-dot"></span><span class="social-dot"></span>
    </div>
  </footer>
</main>
</body>
</html>
```